'CALVENTO' NEW WINE LABEL DESIGN

I am looking for an exceptional and exciting design for a wine label called 'Calvento' meaning 'Lookout'. The design must feature the name 'Calvento', and the word 'Cabernet Sauvignon' in version 1 and 'Sauvignon Blanc' in version 2. It will also need the words 'Valle Central, Chile' at the bottom of the label as a prominent piece of information as well as the vintage 2017. Please produce the work in size 80mm x 100mm. Feel free to use colour in addition to black/white and ensue that the label is easy to read on a shelf placement.
Target Market(s)
SUPERMARKETS & WINE STORES
Requirements
Must have
- EASY TO READ, USE COLOURS LIKE GREEN FOR SAUVIGNON & RED FOR CABERNET SAUVIGNON
- FULL BOTTLE SHOT MUST BE IN PROVIDED DESIGNS. ALL BOTTLE TOPS SHOULD BE QUORLEX STYLE (SCREW TOP)
- PLEASE NOTE THAT LABEL INFORMATION MUSY BE EASY TO READ I.E. VINTAGE, PLACE OF ORGIN ALTHOUGH NOT THE MAIN CONTENT MUST STILL BE CLEAR.
Nice to have
- ARTISTIC REFERENCE LINK TO NAME & ANDES BUT NOT PICTURES OF MOUNTAINS
Should not have
- PICTURES OF GRAPES
- PICTURES OF VINEYARDS
- PICTURES OF MOUNTAINS

```html
<!DOCTYPE html>
<html lang="en">
<head>
<meta charset="utf-8">
<title>Calvento Wine Labels</title>
<link rel="stylesheet" href="https://fonts.googleapis.com/css2?family=Oswald:wght@400;500;600&family=Cormorant+Garamond:wght@500&display=swap">
<style>
  :root {
    --page-bg: #f3f3f3;
    --label-bg: #1b1b1c;
    --label-bg-edge: #121213;
    --band-dark: #242425;
    --band-light: #8a8a8a;
    --text-light: #e9e9e9;
    --text-soft: #c8c8c8;
    --cabernet: #d0222b;
    --cabernet-deep: #8e1a1f;
    --sauvignon: #a9d138;
    --sauvignon-deep: #5f8a1f;
  }
  * { margin: 0; padding: 0; box-sizing: border-box; }
  html, body {
    width: 1168px;
    height: 1200px;
    overflow: hidden;
    background: var(--page-bg);
  }
  .sheet {
    position: relative;
    width: 1168px;
    height: 1200px;
  }
  .label {
    position: absolute;
    top: 171px;
    width: 480px;
    height: 858px;
    background: linear-gradient(90deg, var(--label-bg-edge) 0%, var(--label-bg) 30%, var(--label-bg) 70%, var(--label-bg-edge) 100%);
    color: var(--text-light);
    text-align: center;
  }
  .label--cabernet { left: 64px; --accent: var(--cabernet); --accent-deep: var(--cabernet-deep); }
  .label--sauvignon { left: 624px; --accent: var(--sauvignon); --accent-deep: var(--sauvignon-deep); }

  .pattern-band {
    position: absolute;
    left: 0;
    width: 100%;
    height: 34px;
    background: linear-gradient(90deg, var(--band-dark) 0%, var(--band-light) 50%, var(--band-dark) 100%);
    opacity: 0.55;
  }
  .pattern-band--top { top: 0; }
  .pattern-band--middle { top: 566px; }
  .pattern-band--bottom { top: 824px; }

  .divider {
    position: absolute;
    left: 0;
    width: 100%;
    height: 3px;
    top: 606px;
    background: #0c0c0c;
  }

  .brand-name {
    position: absolute;
    top: 112px;
    left: 0;
    width: 100%;
    font-family: "Oswald", sans-serif;
    font-weight: 600;
    font-size: 92px;
    line-height: 1;
    letter-spacing: 2px;
    color: var(--text-light);
  }
  .vintage {
    position: absolute;
    top: 236px;
    left: 0;
    width: 100%;
    font-family: "Cormorant Garamond", serif;
    font-weight: 500;
    font-size: 21px;
    letter-spacing: 8px;
    color: var(--text-soft);
  }
  .varietal {
    position: absolute;
    top: 284px;
    left: 0;
    width: 100%;
    font-family: "Oswald", sans-serif;
    font-weight: 500;
    font-size: 28px;
    letter-spacing: 1px;
    color: var(--text-light);
  }

  .spec-row {
    position: absolute;
    top: 481px;
    left: 50px;
    width: 380px;
    height: 44px;
    display: flex;
    border-top: 2px solid var(--accent);
  }
  .spec-row__cell {
    flex: 1;
    display: flex;
    align-items: center;
    justify-content: center;
    font-family: "Oswald", sans-serif;
    font-weight: 400;
    font-size: 15px;
    color: var(--text-soft);
  }
  .spec-row__cell + .spec-row__cell { border-left: 2px solid var(--accent); }

  .ridge-art {
    position: absolute;
    top: 650px;
    left: 0;
    width: 100%;
    height: 80px;
    background: linear-gradient(180deg, rgba(0,0,0,0) 0%, var(--accent) 45%, var(--accent-deep) 100%);
    clip-path: polygon(0 100%, 0 70%, 100% 70%, 100% 100%);
  }
  .ridge-art::after { content: none; }

  .origin {
    position: absolute;
    top: 758px;
    left: 0;
    width: 100%;
    font-family: "Cormorant Garamond", serif;
    font-weight: 500;
    font-size: 22px;
    letter-spacing: 7px;
    color: var(--text-light);
  }
</style>
</head>
<body>
<main class="sheet">

  <section class="label label--cabernet">
    <div class="pattern-band pattern-band--top" role="img" aria-label="Decorative geometric border pattern"></div>
    <h1 class="brand-name">CALVENTO</h1>
    <p class="vintage">VINTAGE 2017</p>
    <p class="varietal">CABERNET SAUVIGNON</p>
    <div class="spec-row">
      <span class="spec-row__cell">ALC 13.2%</span>
      <span class="spec-row__cell">PREMIUM WINE</span>
      <span class="spec-row__cell">750 ML (XX OZ.)</span>
    </div>
    <div class="pattern-band pattern-band--middle" role="img" aria-label="Decorative geometric border pattern"></div>
    <div class="divider"></div>
    <div class="ridge-art" role="img" aria-label="Red stylised Andes ridge illustration"></div>
    <p class="origin">VALLE CENTRAL, CHILE</p>
    <div class="pattern-band pattern-band--bottom" role="img" aria-label="Decorative geometric border pattern"></div>
  </section>

  <section class="label label--sauvignon">
    <div class="pattern-band pattern-band--top" role="img" aria-label="Decorative geometric border pattern"></div>
    <h2 class="brand-name">CALVENTO</h2>
    <p class="vintage">VINTAGE 2017</p>
    <p class="varietal">SAUVIGNON BLANC</p>
    <div class="spec-row">
      <span class="spec-row__cell">ALC 13.2%</span>
      <span class="spec-row__cell">PREMIUM WINE</span>
      <span class="spec-row__cell">750 ML (XX OZ.)</span>
    </div>
    <div class="pattern-band pattern-band--middle" role="img" aria-label="Decorative geometric border pattern"></div>
    <div class="divider"></div>
    <div class="ridge-art" role="img" aria-label="Green stylised Andes ridge illustration"></div>
    <p class="origin">VALLE CENTRAL, CHILE</p>
    <div class="pattern-band pattern-band--bottom" role="img" aria-label="Decorative geometric border pattern"></div>
  </section>

</main>
</body>
</html>
```